Monthly Planner & To Do List on dry erase magnetic whiteboard

I'm after 2 x designs for magnetic whiteboards.
1. 17 x 13 inches is a monthly planner. Dates and month can be written in each month and then wiped off and re-written for the next month.
2. 6 x 4 inches - to do list however I don't want this to say To Do on it but will have lines to write on and possibly bullet points to check off.
I have attached below samples of other products (the ones I like the most are the first two - 9.19.52 and 9.20.34). I actually don't like the design of the others but just show them here as an example for layout purposes.
I want something that is modern, slick, simple yet stylish which is what my brand is representative of - smart, modern, organised. It will be printed onto a white board and I only want the print to be in black, no grey shading. I need a more modern font and don't like any of the swirly parts. Just clean and simple but slick.
I would like the size of the day squares to be as large as possible to fit writing in them and also for a section somewhere on the page for additional notes.

• Old style fonts, cartoon style or childish.

```html
<!DOCTYPE html>
<html lang="en">
<head>
<meta charset="UTF-8">
<title>Month Planner</title>
<link href="https://fonts.googleapis.com/css2?family=Bebas+Neue&family=Roboto:wght@400&family=Roboto+Condensed:wght@300&display=swap" rel="stylesheet">
<style>
  :root {
    --page: #ffffff;
    --ink: #000000;
  }
  * { margin: 0; padding: 0; box-sizing: border-box; }
  html, body { width: 1200px; height: 1200px; overflow: hidden; background: var(--page); }
  .planner { position: relative; width: 1200px; height: 1200px; }
  .planner-title {
    position: absolute; left: 97px; top: 172px;
    font-family: "Bebas Neue", sans-serif; font-weight: 400; font-size: 116px; line-height: 1;
    color: var(--ink);
  }
  .planner-label {
    position: absolute; right: 137px; top: 250px;
    font-family: "Roboto Condensed", sans-serif; font-weight: 300;
    font-size: 35px; line-height: 1; color: var(--ink);
  }
  .calendar {
    position: absolute; left: 96px; top: 296px; width: 967px;
    display: grid; grid-template-columns: repeat(7, 1fr);
    column-gap: 2.4px;
  }
  .day-name {
    height: 39px; display: flex; align-items: center; justify-content: center;
    font-family: "Roboto", sans-serif; font-size: 19px;
    background: var(--page); color: var(--ink);
    border: 1.5px solid var(--ink);
    margin-bottom: 3.6px;
  }
  .day-name.weekend { background: var(--ink); color: var(--page); }
  .day { height: 136px; border: 1.5px solid var(--ink); margin-bottom: 2.4px; }
  .day.muted { border-style: dashed; }
  .todo-card {
    position: absolute; left: 824px; top: 893px; width: 202px; height: 134px;
    border: 1.5px solid var(--ink); padding: 14px 14px 0;
    display: flex; flex-direction: column; gap: 10px;
  }
  .todo-item { display: flex; align-items: flex-end; gap: 8px; height: 19px; }
  .todo-box { width: 13px; height: 13px; border: 1.5px solid var(--ink); flex: none; }
  .todo-line { flex: 1; border-bottom: 1px solid var(--ink); height: 100%; }
  .notes-rule {
    position: absolute; left: 96px; top: 1057px; width: 968px; height: 2px;
    background: var(--ink);
  }
  .notes {
    position: absolute; left: 96px; top: 1059px; width: 968px;
  }
  .notes-line { height: 32px; border-bottom: 1px solid var(--ink); }
</style>
</head>
<body>
<main class="planner">
  <h1 class="planner-title">MONTH</h1>
  <p class="planner-label">PLANNER</p>
  <section class="calendar">
    <div class="day-name weekend">SUN</div>
    <div class="day-name">MON</div>
    <div class="day-name">TUE</div>
    <div class="day-name">WED</div>
    <div class="day-name">THR</div>
    <div class="day-name">FRI</div>
    <div class="day-name weekend">SAT</div>

    <div class="day muted"></div><div class="day muted"></div><div class="day"></div><div class="day"></div><div class="day"></div><div class="day"></div><div class="day"></div>
    <div class="day"></div><div class="day"></div><div class="day"></div><div class="day"></div><div class="day"></div><div class="day"></div><div class="day"></div>
    <div class="day"></div><div class="day"></div><div class="day"></div><div class="day"></div><div class="day"></div><div class="day"></div><div class="day"></div>
    <div class="day"></div><div class="day"></div><div class="day"></div><div class="day"></div><div class="day"></div><div class="day"></div><div class="day"></div>
    <div class="day"></div><div class="day"></div><div class="day"></div><div class="day"></div><div class="day"></div>
  </section>
  <section class="todo-card" aria-label="Checklist">
    <div class="todo-item"><span class="todo-box"></span><span class="todo-line"></span></div>
    <div class="todo-item"><span class="todo-box"></span><span class="todo-line"></span></div>
    <div class="todo-item"><span class="todo-box"></span><span class="todo-line"></span></div>
    <div class="todo-item"><span class="todo-box"></span><span class="todo-line"></span></div>
  </section>
  <div class="notes-rule"></div>
  <section class="notes" aria-label="Notes">
    <div class="notes-line"></div>
    <div class="notes-line"></div>
    <div class="notes-line"></div>
  </section>
</main>
</body>
</html>
```